Website for a financial survey consultancy

WHO WE ARE
We're a niche HR consultancy specialising in salary comparison surveys for the financial asset management industry. We position ourselves as a small, highly responsive organisation with a strong personal relationship with each of our 50+ blue-chip clients.

WHAT WE DO
Our business is 80% surveys (= products), 20% consultancy (= services). The surveys are a set of online products which clients interact with to find the information they are interested in.

WHAT WE WANT
We are completely revising our existing marketing website and need a new up-to-date look and feel for the site. We want you to design 2 web pages
- Home page
- Internal content page

More details below in Must Have Priorities.

REFERENCE SITES
- www.pellimorn.com - nice background image
- www.vantrikel.com - ignoring the animations
- www.quorvalen.com
- www.lumiscap.com - clean, fresh, styly but prob not corporate enough
- www.dorvethfunds.com - spacious, beautiful, slightly dated tho
- www.thalbin.co.uk - ignore the colours. Like the simplicity, larger font size (although want to stick with sans-serif fonts for main content)

DELIVERABLES
The final designs should be delivered as one or more PSD files with clearly named layers. All design elements and treatments should be separated out, for example use adjustment layers rather than applied (and subsequently irreversible) adjustments, strokes, shading, etc.

WHAT NEXT
I'll be monitoring the contest every day and can respond to questions fast. You can IM me on Skype or MSN.
Updates

Project Deadline Extended
Reason: Hi folks,

I am extending the deadline to this project as I am travelling this week and therefore will not be able to make a final decision until next Monday. I will try and provide further feedback over the course of this week but I am only going to be online occasionally so be prepared to wait a few days for a reply from me.

Thanks for all the designs so far.

Owen

Target Market(s)

In order of importance, most important first

1. Potential customers - UK & US financial industry HR professionals, short on time. Heard about us already, want to find out more about what we do, confirm relevance for their needs. Core goal - establish credibility: are we properly resourced, will we be around for years to come, are we *real*.

2. Existing customers - UK & US financial industry professionals, short on time, under pressure, want results quickly, minimum faff, expect high quality, slickly presented information. Primary action: login and use surveys.

3. Industry professionals/researchers - probably arriving through blog content, looking to browse and hoover information. Valuable for their ability to spread awareness of who we are amongst their peers.

Industry/Entity Type

Financial

Requirements
Must have
• GENERAL
Style cues - Corporate, professional, financial, stylish, slick, clean, spacious, light
Size - standard 960px grid

NAVIGATION
- [ Home | About us | Surveys | Consulting | Blog ]
- Sub-nav (roll-over dropdown) on About Us, Surveys & Consulting

ALL PAGES
- Site navigation
- Client login (on screen permanently or link to ajaxy in-page pop-up)
- Footer section
- Existing logo (attached)* - this is obviously an important reference point in the design, esp colour

HOME PAGE
- Communicate (link thru to?) survey/consulting split
- Large photo(s)/backdrop (2-3 interchangeable options ideally). Please consider what rights agreement will be necessary for any photos you include in your design.
- Possibly bigger more prominent version of logo
- Strap line/sentence - "Focussed data is the key to success"
- 3 recent blog posts (should look good with and without blog post images)
- Free downloadable PDF research report + supporting blurb

INTERNAL PAGE
- Page title
- Content - typical page will be less than one screenfull
- Level 1 sub-heading
- Level 2 sub-heading
- Bulleted list
- Content supporting image (any image will do - interested in placement, borders (if any), spacing, caption, etc)
- 'Do something' button

* Note: there is some internal debate about this logo at the moment. Some (me) are keen for it to change, some (not me!) are not. If you have an web page design idea/concept that requires an evolution of the logo, go ahead and evolve it. We can explore this further in the design process as necessary, but don't sweat it.
Nice to have
• Values to communicate
- Knowledgeable
- Professional
- Secure
- Personal
- Experienced
- Financial industry specific
- Accurate
- Reliable
Should not have
• - Search box
- Social media links, other than RSS feed button (discrete)

```html
<!DOCTYPE html>
<html lang="en">
<head>
<meta charset="utf-8">
<title>Veltmark Consulting</title>
<link rel="stylesheet" href="https://fonts.googleapis.com/css2?family=Gelasio:wght@400;500&family=Roboto+Condensed:wght@300;400&family=Open+Sans:wght@400;600&display=swap">
<style>
:root{
  --page:#f4f2f0;
  --brand:#680b0b;
  --brand-soft:#c99a98;
  --ink:#3b3434;
  --ink-soft:#555;
  --hero-dark:#1d2329;
  --quote-bg:#3a1316;
  --frame:#cfcfcf;
  --footer:#cfccc6;
  --bubble:#b7b4ae;
  --tab:#ead9d6;
}
*{margin:0;padding:0;box-sizing:border-box}
html,body{width:1108px;height:1200px;overflow:hidden;background:var(--page)}
body{position:relative;font-family:"Gelasio",Georgia,serif;color:var(--ink)}
.abs{position:absolute}

/* header */
.brand-square{left:111px;top:104px;width:34px;height:34px;background:var(--brand)}
.brand-name{left:156px;top:96px;font-size:40px;line-height:48px;color:var(--brand)}
.strapline{left:111px;top:150px;font-size:12px;color:var(--ink-soft)}
.account-tab{left:879px;top:0;width:119px;height:26px;background:var(--tab);font-family:"Open Sans",Arial,sans-serif;font-size:12px;color:var(--ink);text-align:center;line-height:26px}
.main-nav{left:510px;top:164px;width:490px;display:flex;justify-content:space-between;font-size:20px;color:var(--ink)}
.main-nav .current{position:relative}
.main-nav .current::before{content:"";position:absolute;left:-1px;right:-1px;top:-2px;height:3px;background:var(--brand-soft)}

/* hero */
.hero{left:110px;top:195px;width:888px;height:293px;background:var(--frame);padding:4px}
.hero-inner{position:relative;width:100%;height:100%;background:var(--hero-dark);overflow:hidden}
.hero-photo{position:absolute;left:0;top:0;width:360px;height:100%;background:linear-gradient(90deg,#4a5058,#2a3036 70%,var(--hero-dark))}
.hero-quote{position:absolute;left:329px;top:70px;width:551px;height:146px;background:var(--quote-bg);padding:8px 18px;color:#eee}
.hero-quote p{font-family:"Roboto Condensed",Arial,sans-serif;font-weight:300;font-size:22px;line-height:31px;letter-spacing:-.4px}
.hero-quote .who{font-family:"Open Sans",Arial,sans-serif;font-size:11px;line-height:14px;margin-top:8px}
.hero-quote .role{font-style:italic}
.hero-shadow{left:560px;top:488px;width:420px;height:14px;background:radial-gradient(ellipse at top,rgba(0,0,0,.18),transparent 70%)}

/* profile */
h2{font-weight:400;color:var(--brand);font-size:35px;line-height:40px}
.body-copy{font-size:13.5px;line-height:16px;color:var(--ink)}
.profile-title{left:110px;top:513px}
.profile-copy{left:110px;top:560px;width:622px}
.profile-copy p+p{margin-top:16px}
.download-divider{left:760px;top:520px;width:2px;height:142px;background:linear-gradient(transparent,#ccc 50%,transparent)}
.download{left:762px;top:553px;width:236px;height:77px;border-radius:0 8px 8px 0;background:linear-gradient(#e9e8e7,#d2d1cf);display:flex;align-items:center;gap:14px;padding-left:24px}
.download-icon{width:54px;height:56px;background:var(--brand)}
.download-text{font-family:"Roboto Condensed",Arial,sans-serif;color:#2a2a2a;line-height:1}
.download-text b{display:block;font-weight:400;font-size:27px}
.download-text span{font-size:17px}
.rule{left:110px;top:687px;width:886px;border-top:1px dotted #b9b5b2}

/* services */
.service-title{top:712px}
.service-photo{top:757px;width:201px;height:134px;border:1px solid #c9c9c9}
.photo-survey{background:linear-gradient(135deg,#f1f1f1,#c9c9c9)}
.photo-consult{background:linear-gradient(180deg,#9a9a9a,#d8d8d8 60%,#efefef)}
.service-copy{top:754px;width:230px;font-size:13px;line-height:15.2px}
.service-copy p+p{margin-top:14px}
.read-more{top:876px;font-size:13px;color:var(--brand);text-decoration:underline}

/* footer */
.footer{left:0;top:923px;width:1108px;height:277px;background:var(--footer)}
.footer h3{position:absolute;font-weight:400;font-size:33px;color:#444}
.bubble{position:absolute;left:110px;top:100px;width:445px;height:138px;background:var(--bubble);border:1px solid #a9a6a0;border-radius:14px;padding:22px 20px;font-size:13px;line-height:15px;color:#3f3c3a}
.bubble p+p{margin-top:15px}
.bubble-tail{position:absolute;left:170px;top:59px}
.sitemap{position:absolute;left:581px;top:57px;font-size:13.5px;line-height:17.3px;color:#444;list-style:none}
.sitemap .top{font-weight:500}
.sitemap .sub{padding-left:6px;font-size:12.5px}
.contact{position:absolute;left:766px;top:58px;font-size:13px;line-height:15.5px;color:#3c3a38;font-style:normal}
.copy-mark{position:absolute;left:766px;top:180px;width:30px;height:30px;border:2px solid #3c3a38;border-radius:50%;font-size:21px;line-height:26px;text-align:center}
.copy-note{position:absolute;left:766px;top:220px;font-size:13px;color:#3c3a38}
</style>
</head>
<body>

<header>
  <div class="abs brand-square"></div>
  <div class="abs brand-name">Veltmark</div>
  <div class="abs strapline">Focussed data is the key to success</div>
  <div class="abs account-tab">Login &nbsp;|&nbsp; Contact</div>
  <nav class="abs main-nav">
    <span class="current">Home</span><span>|</span><span>About us</span><span>|</span><span>Surveys</span><span>|</span><span>Consulting</span><span>|</span><span>Blog</span>
  </nav>
</header>

<section class="abs hero">
  <div class="hero-inner">
    <div class="hero-photo" role="img" aria-label="Portrait of a businessman in a dark suit, arms folded"></div>
    <blockquote class="hero-quote">
      <p>Veltmark consulting helps us to lorem Ipsum is simply dummy text of the printing and typesetting industry. Lorem Ipsum has been the industry’s standard dummy text.</p>
      <div class="who">Daniel Ferris<br><span class="role">Seniour Marketing Head</span></div>
    </blockquote>
  </div>
</section>
<div class="abs hero-shadow"></div>

<section>
  <h2 class="abs profile-title">Company Profile</h2>
  <div class="abs profile-copy body-copy">
    <p>Lorem Ipsum is simply dummy text of the printing and typesetting industry. Lorem Ipsum has been the industry's standard dummy text.</p>
    <p>When an unknown printer took a galley of type and scrambled it to make a type specimen book. It has survived not only five centuries, but also the leap into electronic typesetting, remaining essentially unchanged.</p>
  </div>
  <div class="abs download-divider"></div>
  <div class="abs download">
    <div class="download-icon"></div>
    <div class="download-text"><b>Download</b><span>research report</span></div>
  </div>
</section>

<div class="abs rule"></div>

<section>
  <h2 class="abs service-title" style="left:110px">Surveys</h2>
  <div class="abs service-photo photo-survey" style="left:110px" role="img" aria-label="Pen filling in a survey answer sheet"></div>
  <div class="abs service-copy" style="left:317px">
    <p>Lorem Ipsum is simply dummy text of the printing and typesetting industry. Lorem Ipsum has been the industry's standard dummy text.</p>
    <p>When an unknown printer took a galley of type and scrambled it to make a type specimen book.</p>
  </div>
  <a class="abs read-more" style="left:485px">read more</a>

  <h2 class="abs service-title" style="left:572px">Consultancy</h2>
  <div class="abs service-photo photo-consult" style="left:572px" role="img" aria-label="Signpost pointing to help, support, advice and guidance against a cloudy sky"></div>
  <div class="abs service-copy" style="left:779px;width:222px">
    <p>Lorem Ipsum is simply dummy text of the printing and typesetting industry. Lorem Ipsum has been the industry's standard dummy text.</p>
    <p>When an unknown printer took a galley of type and scrambled it to make a type specimen book.</p>
  </div>
  <a class="abs read-more" style="left:937px">read more</a>
</section>

<footer class="abs footer">
  <h3 style="left:110px;top:12px">Blog</h3>
  <svg class="bubble-tail" width="52" height="44" viewBox="0 0 52 44"><path d="M2 2 L50 43 L18 43 Z" fill="var(--bubble)"/><path d="M2 2 L50 43 M2 2 L18 43" stroke="#a9a6a0" fill="none"/></svg>
  <div class="bubble">
    <p>• Lorem Ipsum is simply dummy text of the printing and typesetting industry. Lorem Ipsum has been the industry's standard dummy text.</p>
    <p>• When an unknown printer took a galley of type and scrambled it to make a type specimen book.</p>
    <p>• It has survived not only five but also the leap into electronic.</p>
  </div>

  <h3 style="left:580px;top:12px">Sitemap</h3>
  <ul class="sitemap">
    <li class="top">Home</li>
    <li class="top">About Us</li>
    <li class="sub">Sub Page1</li>
    <li class="sub">Sub Page2</li>
    <li class="top">Surveys</li>
    <li class="sub">Sub Page1</li>
    <li class="sub">Sub Page2</li>
    <li class="top">Consulting</li>
    <li class="sub">Sub Page1</li>
    <li class="top">Blog</li>
    <li class="top">Contact</li>
  </ul>

  <h3 style="left:765px;top:12px">Contact</h3>
  <address class="contact">
    Veltmark Consulting Ltd<br>14 Harlow Yard<br>London EC2N 7QT<br><br>+44 (0)20 7946 0318<br>info@veltmarkconsulting.com
  </address>
  <div class="copy-mark">c</div>
  <div class="copy-note">2011 Copyright veltmarkconsulting.com</div>
</footer>

</body>
</html>
```